Brindle Advisory Business Card Design

Business card for business consulting company, using attached logo. We do financial and strategic consulting, and want a clean, professional image with a bit of fun. Our logo is a flat whale tail, which symbolizes the Orca whale, a highly collaborative, group based animal that is very successful in navigating the ocean, protecting the herd, and hunting. We like the logo that is blue and gray on white one one side, but would be open to a blue card with white lettering on the other side... or whatever you'd suggest
Updates
Hi all - I have had the logo modified to take the shadowing off the tail. I will post it on the brief... under a file name called updated logo. thank you Added Saturday, April 25, 2015
Target Market(s)
Small to medium sized businesses ($10M to $500M in revenue per year), financial and sales executives, general managers, attorneys and CPAs
Industry/Entity Type
Financial
Contact Information for Business Card
Want company name, contact info - name, title, telephone, email, website, linkedin, twitter and Facebook. No physical address yet.
Requirements
Must have
- contemporary design, bold, strong, confident but with a bit of fun. prominently feature the logo and the whale tail icon
Nice to have
- unique touches that would differentiate us from a regular card... for example, logo and writing all on front on white background, but on back - logo in white on a blue background
- open to idea of different shapes of card than standard... but not sure
Should not have
- ?

```html
<!DOCTYPE html>
<html lang="en">
<head>
<meta charset="utf-8">
<title>Brindle Advisory – Business Card</title>
<link href="https://fonts.googleapis.com/css2?family=Arimo:wght@400&family=Open+Sans:wght@400&display=swap" rel="stylesheet">
<style>
  :root {
    --brand-blue: #0756a3;
    --paper: #ffffff;
    --frame: #9a9a9a;
    --label-ink: #111111;
    --white: #ffffff;
    --rule: #777777;
  }
  * { margin: 0; padding: 0; box-sizing: border-box; }
  html, body { width: 1200px; height: 467px; overflow: hidden; background: var(--paper); }
  .sheet {
    position: relative;
    width: 1200px; height: 467px;
    border: 1px solid var(--frame);
    font-family: "Arimo", Arial, sans-serif;
  }
  .side-label {
    position: absolute; top: 14px;
    font-size: 29px; color: var(--label-ink);
    transform: translateX(-50%);
  }
  .side-label--front { left: 271px; }
  .side-label--back { left: 889px; }

  /* Front */
  .card-front {
    position: absolute; left: 21px; top: 60px;
    width: 566px; height: 367px;
    background: var(--brand-blue);
  }
  .brand {
    position: absolute; left: 35px; top: 42px;
    display: flex; align-items: flex-start; gap: 8px;
  }
  .brand__mark {
    width: 62px; height: 62px;
    border: 1px solid rgba(255,255,255,0.55);
    border-radius: 8px;
  }
  .brand__text { display: flex; flex-direction: column; align-items: flex-end; }
  .brand__name {
    font-family: "Open Sans", Arial, sans-serif;
    font-size: 40px; line-height: 48px; color: var(--white);
    letter-spacing: -0.5px;
  }
  .brand__tagline {
    font-family: "Open Sans", Arial, sans-serif;
    font-size: 12.5px; color: var(--white); margin-top: -2px;
  }

  /* Back */
  .card-back {
    position: absolute; left: 604px; top: 60px;
    width: 567px; height: 367px;
    border: 1px solid var(--frame);
    background: var(--paper);
    overflow: hidden;
  }
  .card-back__band { position: absolute; left: 0; top: 0; width: 100%; height: 100%; }
  .holder {
    position: absolute; left: 0; top: 30px; width: 100%;
    text-align: center; color: var(--brand-blue);
  }
  .holder__name { font-size: 27px; letter-spacing: 0.5px; line-height: 32px; }
  .holder__rule {
    width: 312px; margin: 2px auto 0;
    border-top: 2px dotted var(--rule);
  }
  .holder__title { font-size: 19px; margin-top: 6px; }
  .contact {
    position: absolute; left: 0; top: 148px; width: 100%;
    text-align: center; color: var(--white); font-size: 20px; line-height: 26px;
  }
  .socials { position: absolute; top: 229px; left: 0; width: 100%; height: 44px; }
  .social {
    position: absolute; top: 0;
    display: flex; align-items: center; gap: 9px;
    color: var(--white); font-size: 20px; line-height: 44px;
  }
  .social--first { left: 58px; }
  .social--second { left: 225px; }
  .social--third { left: 384px; }
  .social__dot { width: 44px; height: 44px; border-radius: 50%; background: var(--white); flex: none; }
  .website {
    position: absolute; left: 0; top: 306px; width: 100%;
    text-align: center; color: var(--white); font-size: 21px;
  }
</style>
</head>
<body>
<div class="sheet">
  <div class="side-label side-label--front">Front</div>
  <div class="side-label side-label--back">Back</div>

  <section class="card-front" aria-label="Card front">
    <div class="brand">
      <div class="brand__mark"></div>
      <div class="brand__text">
        <span class="brand__name">Brindle Advisory</span>
        <span class="brand__tagline">business consulting</span>
      </div>
    </div>
  </section>

  <section class="card-back" aria-label="Card back">
    <svg class="card-back__band" viewBox="0 0 567 367" preserveAspectRatio="none" aria-hidden="true">
      <polygon points="0,116 24,116 42,88 60,116 567,116 567,367 0,367" fill="var(--brand-blue)"/>
    </svg>
    <div class="holder">
      <div class="holder__name">DANIEL HARTLEY</div>
      <div class="holder__rule"></div>
      <div class="holder__title">CEO</div>
    </div>
    <div class="contact">
      <div>+91 02240519376</div>
      <div>daniel@brindleadvisory.in</div>
    </div>
    <div class="socials">
      <div class="social social--first"><span class="social__dot"></span><span>brindle</span></div>
      <div class="social social--second"><span class="social__dot"></span><span>brindle</span></div>
      <div class="social social--third"><span class="social__dot"></span><span>brindle</span></div>
    </div>
    <div class="website">www.brindleadvisory.com</div>
  </section>
</div>
</body>
</html>
```